Vodka label for New Brand called KIRO Vodka

We need a label measuring 3.5 inches wide & 5 inches tall for this vodka bottle. The brand is "KIRO Vodka". This should be the largest font on the label. "Handcrafted in the USA" should be on bottle in small font near the bottom. The tagline "Keeping It Real Onward" also needs to be included anywhere that makes sense in a smaller font than the brand name. Also in smaller font at the bottom/corners- "80 proof, 750 ml, 40% alc/vol" I value the human mind over AI, but am providing a couple designs that were AI generated to give you a better idea where to start and what we are looking for. Thank you!

Target Market(s)

21-45 year olds.

Industry/Entity Type

Alcohol

Colors
0054AA
0677BA
7BADD7
CADEEF
E8F1F8
EB3D1F
EC4F4E
F09395
F8D3D4
FCEDEE

Requirements
Should not have
• You can not use the US flag but can use elements of it.

```html
<!DOCTYPE html>
<html lang="en">
<head>
<meta charset="utf-8">
<title>KIRO Vodka Label</title>
<link href="https://fonts.googleapis.com/css2?family=Saira:wght@500;600&family=Josefin+Sans:wght@400;600&family=Libre+Baskerville&display=swap" rel="stylesheet">
<style>
  :root {
    --bg: #ececef;
    --paper: #ffffff;
    --navy: #27297a;
    --navy-soft: #3a3d8c;
    --red: #e8262b;
    --red-deep: #b83236;
    --ink: #2b2d6e;
  }
  * { margin: 0; padding: 0; box-sizing: border-box; }
  html, body { width: 1200px; height: 1200px; overflow: hidden; background: var(--bg); }
  .canvas { position: relative; width: 1200px; height: 1200px; }
  .label {
    position: absolute; left: 240px; top: 171px;
    width: 720px; height: 858px; background: var(--paper);
  }
  .star-band {
    position: absolute; left: 0; top: 0; width: 720px; height: 167px;
    background: linear-gradient(90deg, var(--navy-soft), var(--navy));
  }
  .tagline-badge {
    position: absolute; left: 277px; top: 36px; width: 166px; height: 84px;
    background: var(--paper); border: 2px solid #b9bcd6; border-radius: 6px;
    display: flex; flex-direction: column; align-items: center; justify-content: center;
    color: var(--ink); text-align: center;
  }
  .tagline-badge .dots { color: var(--red); font-size: 7px; letter-spacing: 2px; line-height: 1; }
  .tagline-badge .small { font-family: "Josefin Sans", sans-serif; font-weight: 600; font-size: 11px; letter-spacing: 0.5px; line-height: 1.2; }
  .tagline-badge .main { font-family: "Libre Baskerville", serif; font-size: 19px; line-height: 1.1; }
  .stripe { position: absolute; height: 29px; background: linear-gradient(90deg, var(--red-deep), var(--red)); }
  .stripe.full { left: 0; width: 720px; }
  .brand {
    position: absolute; left: 0; width: 720px; top: 286px; text-align: center;
    font-family: "Saira", sans-serif; font-weight: 600; font-size: 156px; line-height: 1;
    letter-spacing: 4px;
    background: linear-gradient(90deg, var(--red-deep), var(--red));
    -webkit-background-clip: text; background-clip: text; color: transparent;
  }
  .product {
    position: absolute; left: 0; width: 720px; top: 472px;
    display: flex; align-items: center; justify-content: center; gap: 26px;
    font-family: "Josefin Sans", sans-serif; font-weight: 600; font-size: 46px;
    letter-spacing: 14px; color: var(--navy);
  }
  .product .dash { width: 26px; height: 4px; background: var(--navy); }
  .info-box {
    position: absolute; left: 230px; top: 784px; width: 304px; height: 69px;
    background: var(--paper); border: 2px solid var(--navy);
    display: flex; flex-direction: column; align-items: center; justify-content: center;
    font-family: "Josefin Sans", sans-serif; color: var(--ink); line-height: 1.15;
  }
  .info-box .origin { color: var(--red); font-size: 8px; font-weight: 600; letter-spacing: 1.5px; }
  .info-box .abv { font-size: 19px; letter-spacing: 1.5px; }
  .info-box .proof { font-size: 14px; }
  .volume {
    position: absolute; right: 4px; top: 812px;
    font-family: "Saira", sans-serif; font-size: 14px; color: var(--red-deep);
  }
</style>
</head>
<body>
<main class="canvas">
  <section class="label">
    <div class="star-band" role="img" aria-label="Field of white stars on navy blue"></div>
    <div class="tagline-badge">
      <span class="dots">★★★★★</span>
      <span class="small">KEEPING IT</span>
      <span class="main">REAL</span>
      <span class="small">ONWARD</span>
      <span class="dots">★★★★★</span>
    </div>

    <div class="stripe full" style="top:222px"></div>
    <div class="stripe" style="top:304px;left:0;width:74px"></div>
    <div class="stripe" style="top:387px;left:0;width:74px"></div>
    <div class="stripe" style="top:304px;left:680px;width:40px"></div>
    <div class="stripe" style="top:387px;left:680px;width:40px"></div>

    <h1 class="brand">KIRO</h1>
    <div class="product"><span class="dash"></span><span>VODKA</span><span class="dash"></span></div>

    <div class="stripe full" style="top:568px"></div>
    <div class="stripe full" style="top:671px"></div>
    <div class="stripe full" style="top:774px"></div>

    <div class="info-box">
      <span class="origin">HANDCRAFTED IN THE USA</span>
      <span class="abv">40% ALC/VOL</span>
      <span class="proof">80 PROOF</span>
    </div>
    <span class="volume">750 ML</span>
  </section>
</main>
</body>
</html>
```